Business Card Design for Mabel's Larder

We make food for dogs.
Business Card Design (using the logo designed by you). Our Brand color is a bright canary yellow. For example our signage is predominantly yellow, with the logo in black. I'd like the card also to use that imagery.
Feel free to use the two sides creatively.
Vertical Design is also great.

Industry/Entity Type

Pet food

Contact Information for Business Card

Name, email, website, phone no

Font styles to use
Sans Serif

Colors
59FF00
82FF00
B8FF75
E3FFCB
F4FFEA
FFF300
FFF600
FEFA6F
FFFEC7
FFFEE8

Requirements
Nice to have
• A graphic in the same brush stroke style of the logo shoeing a doggy bowl of food

```html
<!DOCTYPE html>
<html lang="en">
<head>
<meta charset="utf-8">
<title>Mabel's Larder – Business Card</title>
<link rel="stylesheet" href="https://fonts.googleapis.com/css2?family=Oswald:wght@500&family=Arimo:wght@400&display=swap">
<style>
  :root {
    --canary: #fde24f;
    --ink: #111111;
    --paper: #ffffff;
    --stage: #c8c8c8;
    --muted: #9a9a9a;
  }
  * { box-sizing: border-box; margin: 0; padding: 0; }
  html, body { width: 1200px; height: 900px; overflow: hidden; }
  body {
    background: var(--stage);
    display: flex;
    flex-direction: column;
    align-items: center;
    justify-content: center;
    gap: 40px;
    font-family: "Arimo", Arial, sans-serif;
  }
  .card {
    width: 700px;
    height: 400px;
    border-radius: 34px;
    position: relative;
    overflow: hidden;
    box-shadow: 0 6px 14px rgba(0,0,0,0.25);
  }
  .card--front {
    background: var(--canary);
    display: flex;
    align-items: center;
    justify-content: center;
  }
  .brand-name {
    font-family: "Oswald", "Arial Narrow", sans-serif;
    font-weight: 500;
    text-transform: uppercase;
    letter-spacing: 1px;
    line-height: 1;
  }
  .card--front .brand-name { font-size: 78px; color: var(--ink); }

  .card--back { background: var(--paper); }
  .back-brand {
    position: absolute;
    left: 60px;
    top: 70px;
    font-size: 66px;
    color: var(--canary);
  }
  .person {
    position: absolute;
    left: 60px;
    top: 175px;
  }
  .person-name {
    font-family: "Oswald", "Arial Narrow", sans-serif;
    font-weight: 500;
    font-size: 34px;
    color: var(--canary);
    text-transform: uppercase;
    line-height: 1.1;
  }
  .person-role { font-size: 20px; color: var(--ink); margin-top: 2px; }
  .contacts {
    position: absolute;
    left: 60px;
    top: 272px;
    list-style: none;
    font-size: 20px;
    color: var(--ink);
  }
  .contacts li { display: flex; align-items: center; gap: 12px; height: 32px; }
  .contacts svg { width: 20px; height: 20px; fill: var(--canary); flex: none; }
  .contacts .accent { color: var(--canary); }
  .address {
    position: absolute;
    right: 50px;
    top: 220px;
    text-align: right;
    font-size: 19px;
    line-height: 1.3;
    color: var(--ink);
  }
</style>
</head>
<body>
  <section class="card card--front" aria-label="Card front">
    <h1 class="brand-name">Mabel's Larder</h1>
  </section>

  <section class="card card--back" aria-label="Card back">
    <p class="brand-name back-brand">Mabel's Larder</p>
    <div class="person">
      <p class="person-name">Harriet Vale</p>
      <p class="person-role">Managing Director</p>
    </div>
    <ul class="contacts">
      <li>
        <svg viewBox="0 0 24 24" aria-hidden="true"><path d="M6.6 10.8a15.1 15.1 0 0 0 6.6 6.6l2.2-2.2c.3-.3.7-.4 1-.2 1.1.4 2.3.6 3.6.6.6 0 1 .4 1 1V20c0 .6-.4 1-1 1A17 17 0 0 1 3 4c0-.6.4-1 1-1h3.5c.6 0 1 .4 1 1 0 1.3.2 2.5.6 3.6.1.3 0 .7-.2 1z"/></svg>
        044-987 654 321
      </li>
      <li>
        <svg viewBox="0 0 24 24" aria-hidden="true"><path d="M2 5h20v14H2z" opacity=".35"/><path d="M2 5l10 8 10-8v2l-10 8L2 7z"/></svg>
        hello@mabelslarder.com
      </li>
      <li>
        <svg viewBox="0 0 24 24" aria-hidden="true"><path d="M12 2a10 10 0 1 0 0 20 10 10 0 0 0 0-20zm6.9 6h-3a15 15 0 0 0-1.3-3.9A8 8 0 0 1 18.9 8zM12 4c.8 1.2 1.5 2.5 1.9 4h-3.8c.4-1.5 1.1-2.8 1.9-4zM4.3 14a8 8 0 0 1 0-4h3.4a16 16 0 0 0 0 4zm.8 2h3a15 15 0 0 0 1.3 3.9A8 8 0 0 1 5.1 16zM8 8H5.1a8 8 0 0 1 4.3-3.9C8.8 5.3 8.4 6.6 8 8zm4 12c-.8-1.2-1.5-2.5-1.9-4h3.8c-.4 1.5-1.1 2.8-1.9 4zm2.3-6H9.7a14 14 0 0 1 0-4h4.6a14 14 0 0 1 0 4zm.3 5.9c.6-1.2 1-2.5 1.3-3.9h3a8 8 0 0 1-4.3 3.9zm1.7-5.9a16 16 0 0 0 0-4h3.4a8 8 0 0 1 0 4z"/></svg>
        <span>www.<span class="accent">mabelslarder</span>.com</span>
      </li>
    </ul>
    <address class="address" style="font-style:normal">
      17, Orchard Row, Kingsdown<br>
      BS2 8HQ, United Kingdom
    </address>
  </section>
</body>
</html>
```